New Business Card/Website Logo

We need a business card design for a new company based in Sydney. The company focuses mainly in construction in the field of form work and concreting. Attached is the logo being used already which can be used as a base for a new design, the current one is simply too bland and we are looking to spruce it up so it stands out and looks nicer. The logo would also be used on the website which is currently under construction. The attached image has the name, mobile and also the license number which needs to be there. The current email address on there can be removed and can be replaced with the website http://www.pillarvane.com.au, thanks!
Updates

Target Market(s)

Construction industry. Focusing on form work and concreting

Industry/Entity Type

Construction

Requirements
Must have
• License # on card along with website http://www.pillarvane.com.au and mobile phone number
Nice to have
• You have freedom with the design. The current design was a mock up done quite quickly. Please just keep in mind the target audience - construction, thanks.
Should not have
• the breezepost email address can be removed(refer picture) and replaced somewhere on the design with the website http://www.pillarvane.com.au

```html
<!DOCTYPE html>
<html lang="en">
<head>
<meta charset="utf-8">
<title>Pillarvane Construction Services – Business Card</title>
<link rel="stylesheet" href="https://fonts.googleapis.com/css2?family=Jost:wght@400;500&family=Nunito:wght@800;900&display=swap">
<style>
  :root {
    --concrete-light: #d3d9d8;
    --concrete-mid: #bfc7c6;
    --concrete-dark: #aab3b2;
    --ink: #4a5050;
    --ink-soft: #5c6262;
    --mark: #8d9695;
    --emboss-light: rgba(255, 255, 255, 0.55);
    --emboss-dark: rgba(40, 46, 46, 0.45);
  }
  html, body {
    margin: 0;
    padding: 0;
    overflow: hidden;
    background: var(--concrete-mid);
  }
  .card {
    position: relative;
    width: 1200px;
    height: 702px;
    overflow: hidden;
    background:
      radial-gradient(ellipse at 30% 25%, var(--concrete-light) 0%, transparent 60%),
      radial-gradient(ellipse at 80% 85%, var(--concrete-dark) 0%, transparent 65%),
      linear-gradient(160deg, var(--concrete-light), var(--concrete-mid) 55%, var(--concrete-dark));
  }
  .brand-square {
    position: absolute;
    left: 61px;
    top: 40px;
    width: 170px;
    height: 170px;
    background: var(--mark);
  }
  .brand-name {
    position: absolute;
    left: 352px;
    top: 72px;
    margin: 0;
    font-family: "Jost", sans-serif;
    font-weight: 400;
    font-size: 118px;
    line-height: 1;
    letter-spacing: 2px;
    color: var(--ink-soft);
  }
  .tagline {
    position: absolute;
    left: 483px;
    top: 198px;
    margin: 0;
    font-family: "Jost", sans-serif;
    font-weight: 500;
    font-size: 38px;
    line-height: 1;
    letter-spacing: 1px;
    color: var(--ink);
  }
  .embossed {
    font-family: "Nunito", sans-serif;
    font-weight: 900;
    color: var(--ink);
    text-shadow: 2px 2px 2px var(--emboss-dark), -1px -1px 1px var(--emboss-light);
    margin: 0;
    line-height: 1;
    position: absolute;
  }
  .contact {
    right: 74px;
    text-align: right;
  }
  .person-name {
    top: 330px;
    font-size: 60px;
    letter-spacing: 2px;
    right: 96px;
  }
  .website {
    top: 430px;
    font-size: 40px;
    font-weight: 800;
    right: 66px;
  }
  .phone {
    top: 512px;
    font-size: 42px;
    right: 74px;
    letter-spacing: 1px;
  }
  .licence {
    left: 61px;
    top: 620px;
    font-size: 40px;
    letter-spacing: 1px;
  }
</style>
</head>
<body>
  <main class="card">
    <div class="brand-square" aria-hidden="true"></div>
    <h1 class="brand-name">PILLARVANE</h1>
    <p class="tagline">Construction Services</p>

    <p class="embossed contact person-name">Marco Ellery</p>
    <p class="embossed contact website">http://www.pillarvane.com.au</p>
    <p class="embossed contact phone">0491572630</p>

    <p class="embossed licence">Licence: 384926B</p>
  </main>
</body>
</html>
```